Fitness Equipment & Service

I want to make the card eye catching and fun. We are called Corvane Motion Limited and we are based in Wales. We sell, install and service all types of fitness equipment from Skipping ropes, right through the Dumbbells, Kettle bells and Barbells through to state of the art Treadmills, Running Machines and Strength Equipment. We also design and install changing room furniture and lockers.

TYPOGRAPHY
We would like to use Futrura. Futura has an appearance of efficiency and forwardness. The typeface is derived
from simple geometric forms (near-perfect circles, triangles and squares) and is based on strokes of
near-even weight, which are low in contrast. This is most visible in the almost perfectly round stroke of
the o, which is nonetheless slightly ovoid.
The lowercase has tall ascenders, which rise above the cap line. The uppercase
characters present proportions similar to those of classical Roman capitals.

TYPOGRAPHIC CONSIDERATIONS
No Strike though
No Horizontal Scaling
No Drop Shadows
No Effects
Never use less than 120% Leading

OUR CORPORATE COLOURS
BRAND GUIDELINES
We were thinking that our primary colour palette consists of the Acid Green (Pantone 382) and Process Black.

We work closely with tolbrook Ltd and would like to include their name on the card somewhere. I have attached images of the other brands that we work with as an idea or the small icons I have included that illustrate what we do?. I have very kindly been given permission to use any of the images off the files that I have included below, so I hope these help. I will include these below. I would be open to suggestions if it made the card more striking Can you do it?
Updates

Hi All, Just wanted to add a few thoughts but you are the guys with the creative visions (thats why are here) We are based in Wales, UK and we would be open to lots of different ideas on a theme but must be eye catching, Bold and FUN. If you can or think that the Welsh or any dragon could be put in there then go for it (its not a must have) We have also added some ideas for colour but again its over to you!! GO FOR IT ! Thanks and look forward to your visions! Owen

Hi All, Just thought I would sen through the contact details that need to be on the card. (if you want to play around with icons instead of the wording twitter, Facebook, go for it): Corvane Motion Limited Owen Pritchard Managing Director Mob: +44 (0)7382 519 046 e-mail: sales@corvanemotion.co.uk Web: Corvanemotion.co.uk twitter: @motionPostbag Facebook: Corvane Motion Limited

Industry/Entity Type

Fitness

```html
<!DOCTYPE html>
<html lang="en">
<head>
<meta charset="utf-8">
<title>Corvane Motion Limited – Business Card Options</title>
<link rel="stylesheet" href="https://fonts.googleapis.com/css2?family=Lato:wght@400;700;900&family=Jost:wght@300;400&display=swap">
<style>
  :root {
    --sheet-top: #363636;
    --sheet-bottom: #707070;
    --card-black: #1c1c1c;
    --card-black-soft: #2a2a2a;
    --acid-green: #6cb033;
    --acid-green-light: #82c341;
    --tile-white: #ffffff;
    --text-white: #ffffff;
    --text-dark: #1a1a1a;
    --rule-dark: #2b3a1f;
    --rule-grey: #5c5c5c;
    --mark-blue: #1e3d86;
    --label-grey: #d8d8d8;
    --font-text: "Lato", Arial, sans-serif;
    --font-display: "Jost", "Futura", sans-serif;
  }

  * { box-sizing: border-box; margin: 0; padding: 0; }

  html, body {
    width: 1200px;
    height: 541px;
    overflow: hidden;
  }

  .sheet {
    position: relative;
    width: 1200px;
    height: 541px;
    background: linear-gradient(180deg, var(--sheet-top) 0%, var(--sheet-bottom) 100%);
    font-family: var(--font-text);
  }

  .card {
    position: absolute;
    width: 382px;
    height: 229px;
    overflow: hidden;
    background: radial-gradient(ellipse at 70% 40%, var(--card-black-soft) 0%, var(--card-black) 75%);
  }

  .card--front { top: 30px; }
  .card--back  { top: 270px; }
  .option-a { left: 16px; }
  .option-b { left: 410px; }
  .option-c { left: 802px; }

  /* ---------- Front ---------- */
  .front-shapes {
    position: absolute;
    inset: 0;
    width: 382px;
    height: 229px;
  }

  .equipment-icons {
    position: absolute;
    border-radius: 6px;
    background: radial-gradient(ellipse at center, rgba(120,120,120,0.28) 0%, rgba(90,90,90,0.12) 60%, rgba(60,60,60,0) 100%);
  }
  .option-a .equipment-icons { left: 196px; top: 6px; width: 176px; height: 132px; }
  .option-b .equipment-icons { left: 196px; top: 6px; width: 100px; height: 110px; }
  .option-b .equipment-icons--lower { left: 350px; top: 160px; width: 30px; height: 66px; }
  .option-c .equipment-icons { left: 250px; top: 60px; width: 126px; height: 80px; }
  .option-c .equipment-icons--lower { left: 352px; top: 150px; width: 28px; height: 70px; }

  .brand {
    position: absolute;
    left: 16px;
    top: 72px;
    display: flex;
    align-items: center;
    gap: 6px;
  }
  .brand__dot {
    width: 52px;
    height: 52px;
    border-radius: 50%;
    background: var(--mark-blue);
    flex: none;
  }
  .brand__name {
    font-family: var(--font-text);
    font-weight: 900;
    font-size: 12.5px;
    line-height: 1.2;
    color: var(--text-dark);
    text-transform: uppercase;
  }

  .person {
    position: absolute;
    right: 36px;
    top: 39px;
    text-align: right;
  }
  .person__name {
    font-weight: 700;
    font-size: 12.5px;
    line-height: 1.25;
    color: var(--text-white);
  }
  .person__role {
    font-size: 10px;
    line-height: 1.25;
    color: var(--acid-green-light);
  }

  .contact {
    position: absolute;
    text-align: right;
    font-size: 9.5px;
    line-height: 1.3;
    color: var(--text-white);
  }
  .contact--phone { right: 32px; top: 139px; }
  .contact--web   { right: 32px; top: 172px; }
  .contact--social-handle { right: 240px; top: 146px; }
  .contact--social-page   { right: 240px; top: 177px; }

  /* ---------- Back ---------- */
  .back-mark {
    position: absolute;
    left: 123px;
    top: 26px;
    width: 136px;
    height: 136px;
    border-radius: 50%;
    background: var(--mark-blue);
  }
  .back-name {
    position: absolute;
    left: 0;
    right: 0;
    top: 180px;
    text-align: center;
    font-family: var(--font-display);
    font-weight: 300;
    font-size: 12px;
    line-height: 1.3;
    letter-spacing: 0.06em;
    color: var(--text-white);
    text-transform: uppercase;
  }

  .option-label {
    position: absolute;
    top: 474px;
    font-family: var(--font-text);
    font-weight: 400;
    font-size: 32px;
    line-height: 1.2;
    color: var(--label-grey);
  }
  .option-label--a { left: 18px; }
  .option-label--b { left: 414px; }
  .option-label--c { left: 806px; }
</style>
</head>
<body>
<main class="sheet">

  <!-- Front cards -->
  <section class="card card--front option-a">
    <div class="equipment-icons" role="img" aria-label="Faint outline icons of gym equipment: bikes, kettlebells, weights, scales and fruit"></div>
    <svg class="front-shapes" viewBox="0 0 382 229" aria-hidden="true">
      <polygon points="0,0 155,0 203,122 165,229 0,229" fill="var(--acid-green)"/>
      <polygon points="155,0 170,0 218,122 203,122" fill="var(--tile-white)"/>
      <line x1="16" y1="167" x2="150" y2="167" stroke="var(--rule-dark)" stroke-width="1"/>
      <line x1="200" y1="167" x2="350" y2="167" stroke="var(--rule-grey)" stroke-width="1"/>
      <polygon points="153,134 183,134 172,166 142,166" fill="var(--tile-white)"/>
      <polygon points="186,134 218,134 207,166 175,166" fill="var(--tile-white)"/>
      <polygon points="151,170 181,170 170,202 140,202" fill="var(--tile-white)"/>
      <polygon points="184,170 214,170 203,202 173,202" fill="var(--tile-white)"/>
      <g class="icon-phone" fill="var(--acid-green)" transform="translate(189,144)">
        <rect x="0" y="3" width="13" height="7" rx="1.5"/>
        <rect x="-1" y="0" width="15" height="3" rx="1.5"/>
        <circle cx="6.5" cy="6.5" r="2" fill="var(--tile-white)"/>
      </g>
      <g class="icon-screen" transform="translate(186,180)">
        <rect x="0" y="0" width="14" height="9" fill="none" stroke="var(--acid-green)" stroke-width="1.6"/>
        <rect x="5" y="10" width="4" height="2" fill="var(--acid-green)"/>
      </g>
    </svg>
    <div class="brand"><span class="brand__dot"></span><span class="brand__name">Corvane Motion<br>Limited</span></div>
    <div class="person"><p class="person__name">Owen Pritchard</p><p class="person__role">Managing Director</p></div>
    <p class="contact contact--phone">+44 (0)7382 519 046<br>000 . 0000 . 0000</p>
    <p class="contact contact--web">sales@corvanemotion.co.uk<br>Corvanemotion.co.uk</p>
    <p class="contact contact--social-handle">@motionPostbag</p>
    <p class="contact contact--social-page">Corvane Motion Limited</p>
  </section>

  <section class="card card--front option-b">
    <div class="equipment-icons" role="img" aria-label="Faint outline icons of gym equipment: scales, boxing gloves, exercise bike and kettlebell"></div>
    <div class="equipment-icons equipment-icons--lower" role="img" aria-label="Faint outline icons of a treadmill and skipping rope"></div>
    <svg class="front-shapes" viewBox="0 0 382 229" aria-hidden="true">
      <polygon points="0,0 155,0 203,122 165,229 0,229" fill="var(--acid-green)"/>
      <polygon points="155,0 170,0 218,122 203,122" fill="var(--tile-white)"/>
      <line x1="16" y1="167" x2="150" y2="167" stroke="var(--rule-dark)" stroke-width="1"/>
      <line x1="200" y1="167" x2="350" y2="167" stroke="var(--rule-grey)" stroke-width="1"/>
      <polygon points="153,134 183,134 172,166 142,166" fill="var(--tile-white)"/>
      <polygon points="186,134 218,134 207,166 175,166" fill="var(--tile-white)"/>
      <polygon points="151,170 181,170 170,202 140,202" fill="var(--tile-white)"/>
      <polygon points="184,170 214,170 203,202 173,202" fill="var(--tile-white)"/>
      <g fill="var(--acid-green)" transform="translate(189,144)">
        <rect x="0" y="3" width="13" height="7" rx="1.5"/>
        <rect x="-1" y="0" width="15" height="3" rx="1.5"/>
        <circle cx="6.5" cy="6.5" r="2" fill="var(--tile-white)"/>
      </g>
      <g transform="translate(186,180)">
        <rect x="0" y="0" width="14" height="9" fill="none" stroke="var(--acid-green)" stroke-width="1.6"/>
        <rect x="5" y="10" width="4" height="2" fill="var(--acid-green)"/>
      </g>
    </svg>
    <div class="brand"><span class="brand__dot"></span><span class="brand__name">Corvane Motion<br>Limited</span></div>
    <div class="person"><p class="person__name">Owen Pritchard</p><p class="person__role">Managing Director</p></div>
    <p class="contact contact--phone">+44 (0)7382 519 046<br>000 . 0000 . 0000</p>
    <p class="contact contact--web">sales@corvanemotion.co.uk<br>Corvanemotion.co.uk</p>
    <p class="contact contact--social-handle">@motionPostbag</p>
    <p class="contact contact--social-page">Corvane Motion Limited</p>
  </section>

  <section class="card card--front option-c">
    <div class="equipment-icons" role="img" aria-label="Faint outline icons of gym equipment: bench, fruit and exercise bike"></div>
    <div class="equipment-icons equipment-icons--lower" role="img" aria-label="Faint outline icons of a kettlebell and treadmill"></div>
    <svg class="front-shapes" viewBox="0 0 382 229" aria-hidden="true">
      <polygon points="0,0 155,0 203,122 165,229 0,229" fill="var(--acid-green)"/>
      <polygon points="155,0 170,0 218,122 203,122" fill="var(--tile-white)"/>
      <line x1="16" y1="167" x2="150" y2="167" stroke="var(--rule-dark)" stroke-width="1"/>
      <line x1="200" y1="167" x2="350" y2="167" stroke="var(--rule-grey)" stroke-width="1"/>
      <polygon points="153,134 183,134 172,166 142,166" fill="var(--tile-white)"/>
      <polygon points="186,134 218,134 207,166 175,166" fill="var(--tile-white)"/>
      <polygon points="151,170 181,170 170,202 140,202" fill="var(--tile-white)"/>
      <polygon points="184,170 214,170 203,202 173,202" fill="var(--tile-white)"/>
      <g fill="var(--acid-green)" transform="translate(189,144)">
        <rect x="0" y="3" width="13" height="7" rx="1.5"/>
        <rect x="-1" y="0" width="15" height="3" rx="1.5"/>
        <circle cx="6.5" cy="6.5" r="2" fill="var(--tile-white)"/>
      </g>
      <g transform="translate(186,180)">
        <rect x="0" y="0" width="14" height="9" fill="none" stroke="var(--acid-green)" stroke-width="1.6"/>
        <rect x="5" y="10" width="4" height="2" fill="var(--acid-green)"/>
      </g>
    </svg>
    <div class="brand"><span class="brand__dot"></span><span class="brand__name">Corvane Motion<br>Limited</span></div>
    <div class="person"><p class="person__name">Owen Pritchard</p><p class="person__role">Managing Director</p></div>
    <p class="contact contact--phone">+44 (0)7382 519 046<br>000 . 0000 . 0000</p>
    <p class="contact contact--web">sales@corvanemotion.co.uk<br>Corvanemotion.co.uk</p>
    <p class="contact contact--social-handle">@motionPostbag</p>
    <p class="contact contact--social-page">Corvane Motion Limited</p>
  </section>

  <!-- Back cards -->
  <section class="card card--back option-a">
    <div class="back-mark"></div>
    <p class="back-name">Corvane Motion Limited</p>
  </section>
  <section class="card card--back option-b">
    <div class="back-mark"></div>
    <p class="back-name">Corvane Motion Limited</p>
  </section>
  <section class="card card--back option-c">
    <div class="back-mark"></div>
    <p class="back-name">Corvane Motion Limited</p>
  </section>

  <p class="option-label option-label--a">A</p>
  <p class="option-label option-label--b">B</p>
  <p class="option-label option-label--c">C</p>

</main>
</body>
</html>
```